Vel-Trax.ch is looking for business card letterhead and envelope C5 with WOW effect

We need a strong business card for our company Vel-Trax.ch, logo is available. You want a black or dark background on which the logo Stark r% 26 # 252; appears. Letterhead and envelope in C5 format should be in a similar design, but does not have to be We need a strong business card for our company Vel-Trax.ch, logo is available. A black or dark background is desired, on which the logo Stark comes across. The letterhead and the envelope in C5 format should have a similar design.

Target Market(s)

Private customers as well as entrepreneurs

Contact Information for Business Card

E-mail: info@vel-trax.ch
Web.www.Vel-Trax.ch
Tel: +41 ( 0 ) 79 684 3027
Adresse:
Lindenhaldeweg 14
9416 Brenzikon

Hier kann man Icons verwenden für Email,Tel und Adressse

Font styles to use
Other font styles liked:
• Dubai,bold

Colors

Designer to choose colors to be used in the design.

Requirements
Must have
• WOW effect
Nice to have
• R% 26 # 252; back business card with our service listings. - VEHICLE LABELING - SHOP WINDOW LABELING - STICKERS AND MUCH MORE ... in red color

```html
<!DOCTYPE html>
<html lang="en">
<head>
<meta charset="utf-8">
<title>Vel-Trax.ch – Business Card</title>
<link rel="stylesheet" href="https://fonts.googleapis.com/css2?family=Lato:wght@400;900&display=swap">
<style>
  :root {
    --backdrop: #5e5e5e;
    --card: #0a0a0b;
    --edge: #f5c400;
    --accent: #f7c600;
    --name-gold: #e9a81c;
    --ink: #f2f2f2;
    --divider: #5a4a1c;
  }
  * { margin: 0; padding: 0; box-sizing: border-box; }
  html, body {
    width: 1200px;
    height: 900px;
    overflow: hidden;
    background: var(--backdrop);
    font-family: "Lato", sans-serif;
  }
  .canvas {
    position: relative;
    width: 1200px;
    height: 900px;
  }
  .card {
    position: absolute;
    left: 290px;
    width: 620px;
    height: 365px;
    background: var(--card);
    border: 2px solid var(--edge);
    box-shadow: 0 14px 30px rgba(0,0,0,.45);
  }
  .card--brand { top: 55px; }
  .card--contact { top: 480px; }

  .wordmark {
    display: flex;
    align-items: center;
    gap: 16px;
    color: var(--ink);
    font-weight: 900;
    text-transform: uppercase;
    letter-spacing: 1px;
    white-space: nowrap;
  }
  .wordmark__square {
    background: var(--accent);
    flex: none;
  }
  .card--brand .wordmark {
    position: absolute;
    left: 0; right: 0; top: 0; bottom: 0;
    justify-content: center;
    font-size: 52px;
  }
  .card--brand .wordmark__square { width: 62px; height: 62px; }

  .card--contact .wordmark {
    position: absolute;
    left: 44px;
    top: 108px;
    font-size: 28px;
    gap: 12px;
  }
  .card--contact .wordmark__square { width: 34px; height: 34px; }

  .divider {
    position: absolute;
    left: 300px;
    top: 70px;
    width: 1px;
    height: 225px;
    background: var(--divider);
  }
  .details {
    position: absolute;
    left: 330px;
    top: 62px;
    color: var(--ink);
  }
  .details__name {
    color: var(--name-gold);
    font-weight: 900;
    font-size: 27px;
    text-transform: uppercase;
    letter-spacing: .5px;
    line-height: 1.1;
  }
  .details__role {
    font-size: 16px;
    margin-top: 6px;
  }
  .details__address {
    font-style: normal;
    font-size: 16px;
    line-height: 1.35;
    margin-top: 14px;
  }
  .contact-list {
    list-style: none;
    margin-top: 16px;
    font-size: 16px;
  }
  .contact-list li {
    display: flex;
    align-items: center;
    gap: 10px;
    line-height: 1.55;
  }
  .contact-list svg {
    width: 15px;
    height: 15px;
    fill: var(--name-gold);
    flex: none;
  }
</style>
</head>
<body>
<main class="canvas">

  <section class="card card--brand" aria-label="Business card back">
    <div class="wordmark">
      <span class="wordmark__square"></span>
      <span class="wordmark__name">Vel-Trax.ch</span>
    </div>
  </section>

  <section class="card card--contact" aria-label="Business card front">
    <div class="wordmark">
      <span class="wordmark__square"></span>
      <span class="wordmark__name">Vel-Trax.ch</span>
    </div>

    <div class="divider"></div>

    <div class="details">
      <h1 class="details__name">Lukas Brenner</h1>
      <p class="details__role">Founder &amp; CEO</p>
      <address class="details__address">
        Lindenhaldeweg 14<br>
        9416 Brenzikon
      </address>
      <ul class="contact-list">
        <li>
          <svg viewBox="0 0 24 24" aria-hidden="true"><path d="M6.6 10.8a15.1 15.1 0 0 0 6.6 6.6l2.2-2.2a1 1 0 0 1 1-.25 11.4 11.4 0 0 0 3.6.57 1 1 0 0 1 1 1V20a1 1 0 0 1-1 1A17 17 0 0 1 3 4a1 1 0 0 1 1-1h3.5a1 1 0 0 1 1 1c0 1.25.2 2.45.57 3.57a1 1 0 0 1-.25 1z"/></svg>
          <span>+41 ( 0 ) 79 684 3027</span>
        </li>
        <li>
          <svg viewBox="0 0 24 24" aria-hidden="true"><path d="M2 5h20v14H2z M3.5 6.5 12 13l8.5-6.5" stroke="#0a0a0b" stroke-width="1.6"/></svg>
          <span>info@vel-trax.ch</span>
        </li>
        <li>
          <svg viewBox="0 0 24 24" aria-hidden="true"><circle cx="12" cy="12" r="10"/><path d="M2 12h20M12 2c3 3 3 17 0 20M12 2c-3 3-3 17 0 20" stroke="#0a0a0b" stroke-width="1.4" fill="none"/></svg>
          <span>www.Vel-Trax.ch</span>
        </li>
      </ul>
    </div>
  </section>

</main>
</body>
</html>
```